Consultancy Business Card Design

We need a business card design for a new company based in singapore called FortyOne. FortyOne a boutique consultancy firm offering broad-based business solutions, from conception to re-invention, for ventures from new start-ups to long-running traditional businesses.
Its 2 main divisions (Food & Beverage Operations and Construction & Project Management) have access to a wide range of networks, knowledge bases, and resources to service its clients across numerous diverse sectors. This includes, and is not limited to, construction, F&B, and retail.
We are a company that combines the ambition, boldness and energy of one in the 20s with the dedication, level-headedness and dependability of one entering its 30s. Bridging the experiences of the old with ideals of the young, we draw on the positives of both to create a unique synergy.
We hope to see designs that fits our company profile.
Boutique
FortyOne(Company Name)
Marcus Leow (Name)
Principle Consultant (Title)
F&B and Hospitality (Division)
(+65) 8364 5170 (Contact no.)
marcus@fortyone-example.com.sg (Email)

```html
<!DOCTYPE html>
<html lang="en">
<head>
<meta charset="utf-8">
<title>FortyOne – Business Card</title>
<link href="https://fonts.googleapis.com/css2?family=Merriweather:wght@400;700&display=swap" rel="stylesheet">
<style>
  :root {
    --backdrop: #d9d9d9;
    --card: #333333;
    --accent: #d7262c;
    --light: #f4f4f4;
    --muted: #a9a9a9;
    --serif: "Merriweather", Georgia, serif;
  }
  * { box-sizing: border-box; margin: 0; padding: 0; }
  html, body {
    width: 1200px; height: 1000px; overflow: hidden;
    background: var(--backdrop);
    font-family: var(--serif);
  }
  .canvas {
    width: 1200px; height: 1000px;
    display: flex; flex-direction: column; align-items: center; justify-content: center;
    gap: 44px;
  }
  .card {
    position: relative;
    width: 720px; height: 412px;
    background: var(--card);
    box-shadow: 0 10px 28px rgba(0,0,0,.22);
  }
  /* Front */
  .card--front {
    display: flex; align-items: center; justify-content: center; gap: 22px;
  }
  .brand__mark {
    width: 40px; height: 40px; background: var(--accent);
  }
  .brand__name {
    font-weight: 400; font-size: 60px; line-height: 1;
    color: var(--light);
  }
  /* Back */
  .badge {
    position: absolute; left: 64px; top: 236px;
    width: 62px; height: 62px; background: var(--accent);
  }
  .person { position: absolute; left: 146px; top: 222px; }
  .person__name { font-weight: 700; font-size: 25px; color: var(--accent); }
  .person__title { font-size: 18px; color: var(--light); margin-top: 4px; }
  .divider {
    position: absolute; left: 396px; top: 160px;
    width: 3px; height: 96px; background: var(--accent);
  }
  .division {
    position: absolute; left: 432px; top: 168px;
    font-size: 18px; color: var(--muted);
  }
  .contact {
    position: absolute; right: 44px; top: 266px;
    text-align: right; font-size: 18px; color: var(--light); line-height: 1.8;
  }
  .contact .accent { color: var(--accent); }
</style>
</head>
<body>
  <main class="canvas">
    <section class="card card--front" aria-label="Card front">
      <span class="brand__mark"></span>
      <h1 class="brand__name">FortyOne</h1>
    </section>

    <section class="card card--back" aria-label="Card back">
      <div class="badge"></div>
      <div class="person">
        <p class="person__name">Marcus Leow</p>
        <p class="person__title">Principle Consultant</p>
      </div>
      <div class="divider"></div>
      <p class="division">F&amp;B and Hospitality</p>
      <div class="contact">
        <p class="contact__phone"><span class="accent">(+65)</span> 8364 5170</p>
        <p class="contact__email"><span class="accent">marcus</span>@fortyone-example.com.sg</p>
      </div>
    </section>
  </main>
</body>
</html>
```